Labels for essential oils small botlles

We are Slovenia based company Velnira Botanic Ltd. www.velnira-botanic.com We offer essential oils as pure essential oils or blends (mixed) essential oils. We have different kind of essential oils 40+ and blends. We sell in different sizes as: 10ml, 30ml, 50ml and 100ml. But majority is 10ml.
All essential oils are in glass bottles with closer. We will now change bottles style from amber to cobalt blue with black closure (see picture attached)
We would like to have different stile of label for different category of essential oils. Here is link about different categories of essential oils https://www.vialquarry.com/mixing-guides/ . The different style / color could be by note:
- Top notes
- Middle notes
- Base notes
- Mixes – different oils mixed together and named as chill out, deep breath, sleep well, etc
Possible is also differentiation regarding:
• Citrus
• Floral
• Herbaceous
• Camphoraceous
• Spicy
• Resinous
• Woody
• Earthy
• Mixes

On labels should be also pictograms according to REACH directive of EU and label according to CPL (see attached file). We would also like to add EAN code attached on the edge of the label. On label is some text fixed I try to show in pdf attached file and some is variable depends from essential oil and date of production.

Meaning we need general labels for each note or other classification and one for mixes – you could also show your option or classification on something else with story behind.

10 ml roll 30 mm x 70 mm (1,25”x3”) but finial dimensions will follow.

We use Tessaro Qm700 printer. For editing labels we use BarTender which support also EAN codes. We import labels as picture in background or different according to your instructions.

Target Market(s)

Retail, health and wellness, all audiences and web shop

Industry/Entity Type

Health And Wellness

Font styles to use
Other font styles liked:
• GillLigHr is our font but could be different

Colors

Designer to choose colors to be used in the design.

Requirements
Must have
• Label should be as template that we could use for different oils in same group. More in attached document. According to CLP we have to put red pictograms on labels which is not nice and should be some how nicely integrated. on the edge EAB dar code that products could be sell through online.
Nice to have
• Different colours, some symbol as a drop or flower or herb. Logo is not necessary that is on label. We would like that label it self represent our brand.

```html
<!DOCTYPE html>
<html lang="sl">
<head>
<meta charset="utf-8">
<title>Velnira Botanic – Essential Oil Label, Mixes</title>
<link rel="stylesheet" href="https://fonts.googleapis.com/css2?family=Cormorant+Garamond:wght@500&family=DM+Serif+Display&family=Khand:wght@500;600&family=Barlow+Semi+Condensed:wght@400;500&family=Barlow:wght@700&family=Arimo:wght@400;700&display=swap">
<style>
  :root{
    --ink:#3a3a3a;
    --label-bg:#000;
    --teal:#5bc5d1;
    --white:#fff;
    --measure:#2f6fa7;
    --hazard:#e0242b;
    --code-ink:#333;
  }
  *{margin:0;padding:0;box-sizing:border-box}
  html,body{width:1200px;height:1003px;overflow:hidden;background:#fff}
  .sheet{position:relative;width:1200px;height:1003px;border:1.5px solid #555;font-family:"Arimo",sans-serif}
  .brand-title{position:absolute;top:140px;left:0;width:100%;text-align:center;font-family:"Cormorant Garamond",serif;font-weight:500;font-size:42px;letter-spacing:2px;color:var(--ink)}
  .dimensions{position:absolute;left:0;top:0}
  .dim-width{position:absolute;top:329px;left:561px;width:80px;text-align:center;background:#fff;color:var(--measure);font-family:"Arimo",sans-serif;font-size:24px;line-height:30px}
  .dim-height{position:absolute;left:1070px;top:562px;width:60px;text-align:center;transform:rotate(-90deg);background:#fff;color:var(--measure);font-family:"Arimo",sans-serif;font-size:24px;line-height:30px}

  .label{position:absolute;left:160px;top:396px;width:879px;height:366px;background:var(--label-bg);color:var(--white);overflow:hidden}
  .logo-frame{position:absolute;left:36px;top:-3px;width:256px;height:72px;border:3px solid var(--teal);display:flex;align-items:center;justify-content:center}
  .logo-frame span{font-family:"Cormorant Garamond",serif;font-size:17px;letter-spacing:1.5px;color:var(--white);margin-top:4px}
  .category{position:absolute;left:50px;top:336px;width:240px;transform:rotate(-90deg);transform-origin:left top;font-family:"DM Serif Display",serif;font-size:42px;line-height:40px;white-space:nowrap}
  .purity{position:absolute;right:605px;top:98px;font-family:"DM Serif Display",serif;font-size:22px}
  .blend-band{position:absolute;left:104px;top:136px;width:169px;height:35px;background:var(--teal);color:#0e1b1d;font-family:"Khand",sans-serif;font-weight:500;font-size:26px;text-align:right;padding-right:8px;line-height:38px}
  .ingredients{position:absolute;right:605px;top:184px;text-align:right;font-family:"Barlow Semi Condensed",sans-serif;font-size:18px;line-height:25px}
  .blend-number{position:absolute;left:237px;top:300px;width:36px;height:36px;border-radius:50%;background:var(--teal);color:#000;font-family:"Barlow",sans-serif;font-weight:700;font-size:21px;text-align:center;line-height:36px}

  .legal{position:absolute;left:336px;width:510px;font-family:"Barlow Semi Condensed",sans-serif;font-weight:500;font-size:14.6px;white-space:nowrap}
  .legal .key{color:var(--teal)}
  .warning{top:31px;line-height:22.5px;white-space:normal;font-weight:400}
  .hazardous{top:128px;line-height:20px}
  .serial{top:160px;line-height:20px}
  .expiry{top:191px;line-height:20px}
  .volume{top:232px;font-family:"Khand",sans-serif;font-weight:600;font-size:28px;line-height:32px}
  .company{top:282px;line-height:20px;color:var(--teal)}
  .address{top:305px;line-height:20px}

  .barcode-area{position:absolute;left:640px;top:143px;width:205px;height:88px;background:var(--white);color:var(--code-ink);font-family:"Khand",sans-serif;font-weight:600;font-size:46px;line-height:92px;text-align:center;letter-spacing:0.5px}
  .hazards{position:absolute;left:626px;top:279px}

  .specs{position:absolute;top:810px;left:0;width:100%;text-align:center;color:var(--ink);font-family:"Arimo",sans-serif;font-size:22px;line-height:58px}
  .specs b{font-weight:700}
</style>
</head>
<body>
<div class="sheet">
  <div class="brand-title">VELNIRA BOTANIC</div>

  <svg class="dimensions" width="1200" height="1003" aria-hidden="true">
    <g stroke="#9fb7cc" stroke-width="1">
      <line x1="161" y1="315" x2="161" y2="368"/>
      <line x1="1039" y1="315" x2="1039" y2="368"/>
      <line x1="1050" y1="396" x2="1125" y2="396"/>
      <line x1="1050" y1="762" x2="1125" y2="762"/>
      <line x1="200" y1="344" x2="1000" y2="344"/>
      <line x1="1100" y1="435" x2="1100" y2="724"/>
    </g>
    <g fill="var(--measure)">
      <polygon points="161,344 203,333 203,355"/>
      <polygon points="1039,344 997,333 997,355"/>
      <polygon points="1100,396 1089,436 1111,436"/>
      <polygon points="1100,762 1089,722 1111,722"/>
    </g>
  </svg>
  <div class="dim-width">3.00"</div>
  <div class="dim-height">1.25"</div>

  <section class="label">
    <div class="logo-frame"><span>VELNIRA BOTANIC</span></div>
    <div class="category">Essential Oil</div>
    <div class="purity">100% Pure</div>
    <div class="blend-band">Mixes</div>
    <div class="ingredients">Officinalis Oil<br>Citrus Grandis Oil<br>Mentha Viridis Oil</div>
    <div class="blend-number">8</div>

    <p class="legal warning">NEVARNO Povzroča draženje kože. Lahko povzroči alergijski odziv kože. Povzroča hude poškodbe oči. Strupeno za vodne organizme, z dolgotrajnimi učinki. Ne vtihavati prahu, dima, plina, meglice, hlapov razpršila. Nositi zaščitne rokavice obleko, zaščito za obraz in oči.</p>
    <p class="legal hazardous"><span class="key">NEVARNE SNOVI</span> 1,8 cimeol, geraniol</p>
    <p class="legal serial"><span class="key">SERIJSKA ŠTEVILKA</span> 15-600-001277</p>
    <p class="legal expiry">UPORABNO DO 09 / 2016 VSEBINA 10ml</p>
    <p class="legal volume">10ML I 0.3 OZ</p>
    <p class="legal company">Velnira Botanic d.o.o.,</p>
    <p class="legal address">Brezovska 27, 1000 Ljubljana, T 014870293</p>

    <div class="barcode-area">BARCODE</div>

    <svg class="hazards" width="220" height="54" viewBox="0 0 220 54" role="img" aria-label="CLP hazard pictograms: irritant, flammable, environmental hazard, health hazard">
      <g stroke="var(--hazard)" stroke-width="3" fill="#fff">
        <polygon points="27,2 52,27 27,52 2,27"/>
        <polygon points="81,2 106,27 81,52 56,27"/>
        <polygon points="135,2 160,27 135,52 110,27"/>
        <polygon points="189,2 214,27 189,52 164,27"/>
      </g>
      <g fill="#000">
        <rect x="24.5" y="13" width="5" height="17" rx="2"/>
        <circle cx="27" cy="36" r="3"/>
        <path d="M81 14c6 6 8 11 5 17c-2 4-8 4-10 0c-2-4 0-7 2-9c0 3 1 4 3 4c-1-4-1-8 0-12z"/>
        <rect x="71" y="34" width="20" height="3"/>
        <path d="M125 37h22l-5-4h-12z"/>
        <path d="M189 15l4 6h6l-4 6 4 6h-6l-4 6-4-6h-6l4-6-4-6h6z"/>
      </g>
      <g stroke="#000" stroke-width="2" fill="none"><path d="M135 17v17M135 23l-6-5M135 26l6-5"/></g>
    </svg>
  </section>

  <div class="specs">
    <p><b>Font Use :</b> Akhand Soft, Narziss Pro, Cyrillic, DIN Next LT PRO</p>
    <p><b>Font Size :</b> Mixes (7pt), Officinalis Oil... (5pt), Back Side (4.5pt)</p>
  </div>
</div>
</body>
</html>
```